Letterhead and Corporate Stationary Design Project

I would like the following designed:
1. Corporate Letterhead
2. Compliment Slips
3. Business Cards(2)

I have attached word document that outlines the text to be contained for all 3. The logo is fine as is and can be used in the design.
I only need letterhead to be designed for contest, the successful applicant can desisgn other 2 items after being awarded the job

Target Market(s)

Information Technology

Industry/Entity Type

Business

Requirements
Must have
• Border around entire letter that matches colours in logo
Clearly identifiable letterhead and footer
Nice to have
• Watermark

```html
<!DOCTYPE html>
<html lang="en">
<head>
<meta charset="utf-8">
<title>Corvanta Business Solutions – Letterhead</title>
<link rel="stylesheet" href="https://fonts.googleapis.com/css2?family=Carlito:wght@400;700&display=swap">
<style>
  :root {
    --frame-navy: #2a4a9f;
    --frame-mid: #3f66c4;
    --frame-light: #7d9fe0;
    --brand-blue: #3a8fd6;
    --ink: #1a1a1a;
    --rule-blue: #4a7bd0;
    --mark-blue: #c9d4ee;
    --mark-grey: #e6e6e6;
    --mark-violet: #b7b5d4;
    --paper: #ffffff;
    --backdrop: #ffffff;
  }
  * { box-sizing: border-box; margin: 0; padding: 0; }
  html, body {
    width: 849px; height: 1200px; overflow: hidden;
    background: var(--backdrop);
  }
  .letterhead {
    position: relative;
    width: 849px; height: 1200px;
    background: var(--paper);
    font-family: "Carlito", "Calibri", sans-serif;
    color: var(--ink);
  }
  .frame {
    position: absolute;
    pointer-events: none;
  }
  .frame--outer {
    inset: 6px;
    border: 9px solid var(--frame-navy);
  }
  .frame--middle {
    inset: 19px;
    border: 2px solid var(--frame-mid);
  }
  .frame--inner {
    inset: 24px;
    border: 1px solid var(--frame-light);
  }
  .brand {
    position: absolute;
    left: 70px; top: 100px;
    display: flex; align-items: center; gap: 12px;
  }
  .brand__dot {
    width: 34px; height: 34px;
    border-radius: 50%;
    background: var(--brand-blue);
  }
  .brand__name {
    font-size: 42px;
    font-weight: 700;
    color: var(--brand-blue);
    letter-spacing: 0.5px;
    line-height: 1;
  }
  .contact {
    position: absolute;
    left: 528px; top: 84px;
    height: 126px;
    padding-left: 22px;
    border-left: 2px solid var(--rule-blue);
    font-size: 14.5px;
    line-height: 18.6px;
    padding-top: 14px;
  }
  .watermark {
    position: absolute;
    left: 115px; top: 505px;
    width: 610px; height: 550px;
    border-radius: 48% 52% 46% 54%;
    background:
      radial-gradient(circle at 33% 30%, var(--mark-blue) 0%, rgba(201,212,238,0.6) 30%, rgba(201,212,238,0) 52%),
      radial-gradient(circle at 16% 72%, var(--mark-grey) 0%, rgba(230,230,230,0) 28%),
      radial-gradient(circle at 70% 78%, var(--mark-violet) 0%, rgba(183,181,212,0) 32%);
    opacity: 0.85;
  }
  .footer {
    position: absolute;
    left: 0; right: 0; top: 1135px;
    text-align: center;
    font-size: 14.5px;
  }
  .footer__sep {
    display: inline-block;
    width: 2px; height: 17px;
    background: var(--rule-blue);
    vertical-align: -3px;
    margin: 0 7px;
  }
</style>
</head>
<body>
  <main class="letterhead">
    <div class="frame frame--outer"></div>
    <div class="frame frame--middle"></div>
    <div class="frame frame--inner"></div>

    <header>
      <div class="brand">
        <span class="brand__dot"></span>
        <span class="brand__name">corvanta</span>
      </div>
      <address class="contact" style="font-style:normal">
        Corvanta Business Solutions<br>
        Harbour House<br>
        22 Mill Street, Kilbrook,<br>
        Co. Wexford, Ireland<br>
        www.corvanta.ie<br>
        tele: +353 53 9140517
      </address>
    </header>

    <div class="watermark" role="img" aria-label="Faint brand watermark in soft blue, grey and violet tones"></div>

    <footer class="footer">
      Corvanta Business Solutions Limited<span class="footer__sep"></span>Company Registration 512846<span class="footer__sep"></span>VAT No IE7315846K
    </footer>
  </main>
</body>
</html>
```